Lucky Orbit Fun Casino Entertainment

Looking to update my business card and make it look more modern, stand out and eye catching.
We are are fun casino business in Australia (primarily Sydney). Blackjack and Roulette are our most popular games although we have pretty much every game available for hire that you would find in a real casino. The final design would need to be sleek and appeal to the more upmarket corporate sector.
We mainly cater for Corporate Events, Private Parties, Fundraising Events, Team Building, Poker Tournaments
I think I'd prefer the colour Black.

Target Market(s)

High-end Corporate

Industry/Entity Type

Events

Contact Information for Business Card

Dale Hutchins
Director
1300 482 617
0431 758 209
info@luckyorbit.com.au
www.luckyorbit.com.au
Facebook & Instagram @luckyorbitshows (proper social icons preferred)

Colors
000000
0255a3

Requirements
Must have
• Front side:
• Logo
• Contact details
• 'Australia's #1 Fun Casino Specialists'
• Back:
• Logo
Nice to have
• Back:
• Corporate Events
• Private Parties
• Poker Tournaments
• Fundraising
• Props & Theming
• Photo Booth
• Horse Racing Events
• The Vegas Sign attached, maybe on the back of the card in the background...?

```html
<!DOCTYPE html>
<html lang="en">
<head>
<meta charset="utf-8">
<title>Lucky Orbit Fun Casino Entertainment – Business Card</title>
<link rel="stylesheet" href="https://fonts.googleapis.com/css2?family=Montserrat:wght@500;600;700&family=Questrial&display=swap">
<style>
  :root {
    --page: #1c1d20;
    --card: #222326;
    --card-edge: #2b2c30;
    --gold: #f6b80c;
    --gold-light: #ffd233;
    --blue: #1e9ad8;
    --blue-deep: #0255a3;
    --ink: #141414;
    --text: #e8e8e8;
    --muted: #bdbdbd;
  }
  * { box-sizing: border-box; margin: 0; padding: 0; }
  html, body { width: 1200px; height: 800px; overflow: hidden; }
  body {
    background: var(--page);
    display: flex;
    flex-direction: column;
    align-items: center;
    justify-content: center;
    gap: 22px;
    font-family: "Questrial", sans-serif;
  }
  .card {
    position: relative;
    width: 620px;
    height: 354px;
    background: var(--card);
    border-radius: 18px;
    overflow: hidden;
    box-shadow: 0 12px 30px rgba(0,0,0,.45);
  }
  .brand {
    position: absolute;
    left: 40px;
    top: 70px;
    width: 250px;
    display: flex;
    flex-direction: column;
    align-items: center;
    gap: 16px;
  }
  .brand-dot {
    width: 96px; height: 96px;
    border-radius: 50%;
    background: var(--gold);
  }
  .brand-name {
    font-family: "Montserrat", sans-serif;
    font-weight: 700;
    font-size: 34px;
    letter-spacing: 1px;
    color: var(--gold);
    text-transform: uppercase;
  }
  .divider {
    position: absolute;
    left: 320px;
    top: 60px;
    width: 1px;
    height: 190px;
    background: linear-gradient(transparent, var(--gold), transparent);
  }
  .contact { position: absolute; left: 350px; top: 56px; color: var(--text); }
  .contact-name {
    font-family: "Montserrat", sans-serif;
    font-weight: 600;
    font-size: 19px;
    color: var(--gold);
    text-transform: uppercase;
  }
  .contact-role { font-size: 14px; color: var(--muted); margin-bottom: 14px; }
  .contact-list { list-style: none; font-size: 14px; line-height: 25px; }
  .contact-list li { display: flex; align-items: center; gap: 10px; }
  .icon { width: 17px; height: 17px; flex: none; }
  .social { display: flex; align-items: center; gap: 6px; margin-top: 10px; font-size: 14px; }
  .social-dot { width: 17px; height: 17px; border-radius: 50%; background: var(--gold); }
  .social-dot + span { margin-left: 4px; }
  .band {
    position: absolute;
    left: 0; right: 0; bottom: 24px;
    height: 38px;
    display: flex; align-items: center; justify-content: center;
    font-family: "Montserrat", sans-serif;
    font-weight: 600;
    font-size: 16px;
    letter-spacing: 2px;
  }
  .band-gold { background: linear-gradient(var(--gold-light), var(--gold)); color: var(--ink); }
  .band-blue { background: linear-gradient(var(--blue), var(--blue-deep)); color: #fff; }
  .services { position: absolute; left: 350px; top: 58px; list-style: none; color: var(--text); font-size: 16px; line-height: 28px; }
  .services li { display: flex; align-items: center; gap: 12px; }
  .chip {
    width: 15px; height: 15px; border-radius: 50%;
    background: #fff;
    border: 3px dashed var(--blue-deep);
  }
</style>
</head>
<body>

<section class="card card-front" aria-label="Business card front">
  <div class="brand">
    <span class="brand-dot"></span>
    <span class="brand-name">Lucky Orbit</span>
  </div>
  <span class="divider"></span>
  <div class="contact">
    <p class="contact-name">Dale Hutchins</p>
    <p class="contact-role">Director</p>
    <ul class="contact-list">
      <li>
        <svg class="icon" viewBox="0 0 20 20"><circle cx="10" cy="10" r="10" fill="#f6b80c"/><path d="M7 5l2 2-1 1.5c.6 1.5 2 2.9 3.5 3.5L13 11l2 2-1.5 1.5C9.5 14 6 10.5 5.5 6.5z" fill="#141414"/></svg>
        <span>1300 482 617</span>
      </li>
      <li>
        <svg class="icon" viewBox="0 0 20 20"><circle cx="10" cy="10" r="10" fill="#f6b80c"/><rect x="7" y="4.5" width="6" height="11" rx="1" fill="none" stroke="#141414" stroke-width="1.5"/></svg>
        <span>0431 758 209</span>
      </li>
      <li>
        <svg class="icon" viewBox="0 0 20 20"><circle cx="10" cy="10" r="10" fill="#f6b80c"/><rect x="5" y="6.5" width="10" height="7" fill="none" stroke="#141414" stroke-width="1.4"/><path d="M5 6.5l5 4 5-4" fill="none" stroke="#141414" stroke-width="1.4"/></svg>
        <span>info@luckyorbit.com.au</span>
      </li>
      <li>
        <svg class="icon" viewBox="0 0 20 20"><circle cx="10" cy="10" r="10" fill="#f6b80c"/><circle cx="10" cy="10" r="5" fill="none" stroke="#141414" stroke-width="1.4"/><path d="M5 10h10M10 5c-2.5 3-2.5 7 0 10M10 5c2.5 3 2.5 7 0 10" fill="none" stroke="#141414" stroke-width="1.2"/></svg>
        <span>www.luckyorbit.com.au</span>
      </li>
    </ul>
    <div class="social">
      <span class="social-dot"></span>
      <span class="social-dot"></span>
      <span>@luckyorbitshows</span>
    </div>
  </div>
  <div class="band band-gold">Australia's #1 Fun Casino Specialists</div>
</section>

<section class="card card-back" aria-label="Business card back">
  <div class="brand">
    <span class="brand-dot"></span>
    <span class="brand-name">Lucky Orbit</span>
  </div>
  <span class="divider"></span>
  <ul class="services">
    <li><span class="chip"></span>Corporate Events</li>
    <li><span class="chip"></span>Private Parties</li>
    <li><span class="chip"></span>Poker Tournaments</li>
    <li><span class="chip"></span>Fundraising</li>
    <li><span class="chip"></span>Props &amp; Theming</li>
    <li><span class="chip"></span>Photo Booth</li>
    <li><span class="chip"></span>Horse Racing Events</li>
  </ul>
  <div class="band band-blue">www.luckyorbit.com.au</div>
</section>

</body>
</html>
```